App landing page and Amber Nook template

I am building a web-based app to help people manage their lives. The app divides their life into 4 categories, Self, Relationships, Career, and Finance. I need a landing page for this application which will feature as a dashboard for each of the categories. The page will be dynamically updated as updates are received from the app. The logo will be a key feature of the page. There will be a menu to the left-hand side. A banner at the top will include interactive icons for the user to navigate the site, manage their account and logout.
I also need a template page for users to present the Ambers Nook to the end users where users can store passwords, important documents, and other important information. This template will present Secrets in either a list format or in an itemized box format.
I have attached the Application Logo for reference.

```html
<!DOCTYPE html>
<html lang="en">
<head>
<meta charset="UTF-8">
<title>Bright Path – Dashboard</title>
<link href="https://fonts.googleapis.com/css2?family=Montserrat:wght@400;500;600;700&display=swap" rel="stylesheet">
<style>
  :root{
    --brand-blue:#0b5fa5;
    --ink:#111111;
    --text:#2a2a2a;
    --label:#2e2e2e;
    --white:#ffffff;
    --hero-light:#e6ecee;
    --hero-mid:#c4cfd3;
    --hero-warm:#8f7d69;
    --hero-cool:#8c9aa3;
    --hero-dark:#3a3436;
  }
  *{box-sizing:border-box;margin:0;padding:0}
  html,body{width:1200px;height:1143px;overflow:hidden;background:var(--white)}
  body{font-family:'Montserrat',sans-serif;color:var(--text);position:relative}

  .top-bar{position:absolute;left:0;top:0;width:1200px;height:70px}
  .menu-toggle{position:absolute;left:114px;top:26px;width:21px;height:16px;display:flex;flex-direction:column;justify-content:space-between}
  .menu-toggle span{display:block;height:3px;background:var(--ink);border-radius:1px}
  .nav-action{position:absolute;top:22px;display:flex;align-items:center;gap:10px;font-size:11.5px;font-weight:600;color:var(--ink);text-decoration:none;letter-spacing:.2px}
  .nav-action svg{width:24px;height:24px}
  .nav-logout{left:808px}
  .nav-account{left:962px}

  .hero{position:absolute;left:0;top:86px;width:1200px;height:611px;overflow:hidden}
  .hero-photo{position:absolute;inset:0;background:
      radial-gradient(ellipse 220px 300px at 560px 420px,rgba(70,90,80,.35),rgba(70,90,80,0)),
      radial-gradient(ellipse 200px 260px at 1120px 420px,rgba(40,30,40,.55),rgba(40,30,40,0)),
      radial-gradient(ellipse 260px 160px at 820px 520px,rgba(230,232,234,.45),rgba(230,232,234,0)),
      linear-gradient(90deg,var(--hero-light) 0%,var(--hero-light) 30%,var(--hero-mid) 42%,var(--hero-warm) 60%,var(--hero-cool) 78%,var(--hero-dark) 100%)}
  .hero-fade{position:absolute;inset:0;background:linear-gradient(90deg,rgba(235,240,242,.9) 0%,rgba(235,240,242,.6) 30%,rgba(235,240,242,0) 48%)}
  .hero-top{position:absolute;left:0;top:0;width:1200px;height:200px}

  .brand{position:absolute;left:0;top:150px;width:1200px;text-align:center}
  .brand-name{display:inline-flex;align-items:center;gap:8px;font-size:20px;font-weight:700;color:var(--brand-blue);letter-spacing:1px;background:var(--white);padding:9px 16px;border-radius:4px}
  .brand-name i{display:inline-block;width:14px;height:14px;border-radius:50%;background:var(--brand-blue)}

  .hero-title{position:absolute;left:73px;top:297px;font-size:38px;font-weight:600;color:var(--ink);letter-spacing:.5px;line-height:38px}
  .hero-tagline{position:absolute;left:73px;top:367px;font-size:30.5px;font-weight:600;color:var(--brand-blue);line-height:31px;letter-spacing:.3px}
  .hero-text{position:absolute;left:73px;top:426px;width:340px;font-size:15.5px;line-height:38.5px;color:var(--text)}

  .categories{position:absolute;left:0;top:760px;width:1200px;height:250px}
  .links{position:absolute;left:0;top:0}
  .category{position:absolute;top:32px;width:200px;margin-left:-100px;text-align:center}
  .badge{display:flex;align-items:center;justify-content:center;margin:0 auto;width:110px;height:110px;border-radius:50%;background:var(--brand-blue);box-shadow:0 0 0 6px #fff,0 0 0 8px var(--brand-blue)}
  .badge svg{width:58px;height:58px}
  .category h3{margin-top:61px;font-size:22px;font-weight:500;color:var(--label);letter-spacing:.5px}

  .site-footer{position:absolute;left:0;top:1070px;width:1200px;height:73px;background:var(--brand-blue);color:var(--white);display:flex;align-items:center;justify-content:center;font-size:15px;font-weight:600;letter-spacing:.2px}
</style>
</head>
<body>

<header class="top-bar">
  <div class="menu-toggle" aria-label="Menu"><span></span><span></span><span></span></div>
  <a class="nav-action nav-logout" href="#">
    <svg viewBox="0 0 24 24"><circle cx="10" cy="7" r="5" fill="var(--brand-blue)"/><path d="M1 22c0-6 4-9 9-9s6 1 7 2v7z" fill="var(--brand-blue)"/><circle cx="18.5" cy="18.5" r="4.5" fill="var(--brand-blue)" stroke="#fff" stroke-width="1.5"/><path d="M16.5 18.5h4M18.5 16.5v4" stroke="#fff" stroke-width="1.5"/></svg>
    LOG OUT
  </a>
  <a class="nav-action nav-account" href="#">
    <svg viewBox="0 0 24 24"><circle cx="12" cy="12" r="11" fill="none" stroke="var(--brand-blue)" stroke-width="1.8"/><circle cx="12" cy="9" r="4" fill="var(--brand-blue)"/><path d="M5 19c1.5-3.5 4-5 7-5s5.5 1.5 7 5" fill="var(--brand-blue)"/></svg>
    MY ACCOUNT
  </a>
</header>

<section class="hero">
  <div class="hero-photo" role="img" aria-label="Photo of three colleagues reviewing papers around a laptop in a bright office"></div>
  <div class="hero-fade"></div>
  <svg class="hero-top" viewBox="0 0 1200 200" preserveAspectRatio="none">
    <path d="M0 0 H1200 V2 C1140 -2 1110 -4 1080 0 C900 20 720 100 600 100 C480 100 300 20 120 0 C90 -4 60 -2 0 2 Z" fill="#fff"/>
    <path d="M100 -17 C300 -5 470 50 600 120 C730 50 900 -5 1100 -17" fill="none" stroke="var(--brand-blue)" stroke-width="4"/>
    <path d="M100 8 C300 18 470 70 600 140 C730 70 900 18 1100 8" fill="none" stroke="#fff" stroke-width="5"/>
  </svg>
  <h1 class="hero-title" style="top:211px">WELCOME TO</h1>
  <h2 class="hero-tagline" style="top:281px">BRIGHT PATH LIVE BETTER</h2>
  <p class="hero-text" style="top:340px">Lorem ipsum dolor sit amet, consectetur adipiscing elit, sed do eiusmod tempor incididunt ut labore</p>
</section>

<div class="brand"><span class="brand-name"><i></i>BRIGHT PATH</span></div>

<section class="categories">
  <svg class="links" width="1200" height="250" viewBox="0 0 1200 250">
    <g fill="none" stroke="var(--brand-blue)" stroke-width="1.5" stroke-dasharray="5 4">
      <path d="M280 76 C320 68 360 68 400 78"/>
      <path d="M540 113 C570 128 620 133 660 124"/>
      <path d="M800 96 C840 90 880 90 920 95"/>
    </g>
  </svg>
  <div class="category" style="left:211px">
    <span class="badge"><svg viewBox="0 0 48 48" fill="none" stroke="#fff" stroke-width="1.8" stroke-linecap="round" stroke-linejoin="round"><circle cx="24" cy="10" r="4.5"/><path d="M17 44V26l-4-3 5-7h12l5 7-4 3v18M24 30v14"/><path d="M7 16l1.2 2.4 2.6.4-1.9 1.8.5 2.6L7 22l-2.4 1.2.5-2.6-1.9-1.8 2.6-.4zM41 16l1.2 2.4 2.6.4-1.9 1.8.5 2.6L41 22l-2.4 1.2.5-2.6-1.9-1.8 2.6-.4z"/></svg></span>
    <h3>SELF</h3>
  </div>
  <div class="category" style="left:471px">
    <span class="badge"><svg viewBox="0 0 48 48" fill="none" stroke="#fff" stroke-width="1.8" stroke-linecap="round" stroke-linejoin="round"><path d="M3 18l8-5 6 2 7-3 7 3 6-2 8 5"/><path d="M3 18l6 12 4 2M45 18l-6 12-4 2"/><path d="M24 12l-7 6 3 2 6-3 10 9-3 4-4-4M33 29l-3 3-4-4M30 32l-3 3-4-4M27 35l-3 2-8-7"/></svg></span>
    <h3>RELATIONSHIPS</h3>
  </div>
  <div class="category" style="left:730px">
    <span class="badge"><svg viewBox="0 0 48 48" fill="none" stroke="#fff" stroke-width="1.8" stroke-linecap="round" stroke-linejoin="round"><circle cx="26" cy="7" r="3.5"/><path d="M24 12l-6 10 7 4-3 10M18 22l-6 4M24 12l6 6 6-2M21 31l-8 6"/><path d="M20 44l10-10 5 4 9-11M38 27h6v6"/><rect x="4" y="12" width="9" height="7" rx="1"/></svg></span>
    <h3>CAREER</h3>
  </div>
  <div class="category" style="left:990px">
    <span class="badge"><svg viewBox="0 0 48 48" fill="none" stroke="#fff" stroke-width="1.8" stroke-linecap="round" stroke-linejoin="round"><path d="M14 6h10l-3 6h-4z"/><path d="M17 12C9 17 5 24 5 31c0 6 4 9 10 9h6"/><circle cx="25" cy="33" r="8"/><path d="M27 29.5h-3a1.5 1.5 0 000 3h2a1.5 1.5 0 010 3h-3M25 28v1.5M25 35.5V38"/><ellipse cx="38" cy="21" rx="6" ry="2.5"/><path d="M32 21v14c0 1.4 2.7 2.5 6 2.5s6-1.1 6-2.5V21M32 25.5c0 1.4 2.7 2.5 6 2.5s6-1.1 6-2.5M32 30c0 1.4 2.7 2.5 6 2.5s6-1.1 6-2.5"/></svg></span>
    <h3>FINANCE</h3>
  </div>
</section>

<footer class="site-footer">© COPYRIGHTS 2024 BRIGHT PATH . ALL RIGHTS RESERVED.</footer>

</body>
</html>
```